■レイアウトの希望について
◎2カラムで、必要に応じて上ナビも入れてください。
※全体の左右を970pxで、ナビの左右サイズを300pxでお願いします。
◎写真やイラストなどのイメージ画像は、最低1点以上入れてください。(有料画像も可)
※現サイトのイラストは自由に使用ください。

■内容について
◎サイト名のロゴは現行のものでなく新たにご提案ください。
※フォントを使用したものでOKです。
◎ヘッダーはスマホサイズになった場合のことも考えて作成してください。
※サイト名の周りは適当にキャッチを入れていただくか、文字を○○○○の形で入れてもかまいません。
◎トップページに入れる文章はできていますが、文字数が少ないのでバランスが悪ければ○○○○の形でプラスしてください。
◎ナビに入れるタイトルはページ構成から抜き出して入れてください。
※上ナビも入れる場合は項目をご提案ください。(左右ナビと変えてもダブってもOK)
※新聞奨学金を目立たせたいので、ナビを工夫されても良いかと思われます。
◎文章とページ構成は以下からダウンロードしてください。
http://www.qx5.co.jp/rmt.zip
基本的にはお任せですが、派手な色やくすんだ色は避けてください。(バランスの良い、落ち着いた色が希望)
納品ファイルは、JPG形式 (.jpg)またはPNG形式 (.png)のいずれかひとつと、イラストレーター形式 (.ai) またはフォトショップ形式 (.psd) のいずれかひとつの、計2ファイルに変更させていただきます。
申し訳ございませんが、ご了承ください。
提案の締め切り日を2日間延ばして6月20日にしました。

第一希望の新聞奨学金ページへの誘導方法がうまく、その他のアイデアも多くいただきました。
それに加え、全体のバランスや色使いが好みだったので、決めさせていただきました。
また、修正依頼などもすぐに対応いただき、助かりました。

多くのご提案をいただき、ありがとうございました。
結局は主観的な好みで決めさせていただきましたが、迷ったご提案も数点ありました。
なお、締切日ギリギリのご提案は、修正依頼が出せないので、良いご提案も見送らせていただいたものもありました。

```html
<!DOCTYPE html>
<html lang="ja">
<head>
<meta charset="utf-8">
<title>奨学金ガイド</title>
<link rel="stylesheet" href="https://fonts.googleapis.com/css2?family=Noto+Sans+JP:wght@400;500;700&display=swap">
<style>
:root{
  --teal:#5fae9f;
  --teal-dark:#3f8f80;
  --accent:#c0392b;
  --leaf:#dfe8b4;
  --leaf-line:#c5d38b;
  --leaf-ink:#3d4a1e;
  --ink:#333333;
  --muted:#666666;
  --rule:#dddddd;
  --page:#f3f4f2;
  --card:#ffffff;
  --navy:#1f4f7a;
  --navy-light:#3c78a8;
  --cta:#e07b39;
}
*{box-sizing:border-box;margin:0;padding:0}
html,body{width:1200px;height:3060px;overflow:hidden}
body{background:var(--page);font-family:"Noto Sans JP",sans-serif;color:var(--ink);position:relative}

.hero{position:absolute;left:0;top:0;width:1200px;height:740px;
  background:linear-gradient(180deg,#5d8fc4 0%,#9cc2e4 45%,#d4e6f2 70%,#7c9a6e 86%,#6b8a5f 100%)}
.brand{position:absolute;left:70px;top:22px;display:flex;align-items:center;gap:14px}
.brand-mark{width:46px;height:46px;background:#fff;border-radius:6px}
.brand-tag{font-size:15px;color:#fff;font-weight:500;line-height:1.2}
.brand-name{font-size:34px;color:#fff;font-weight:700;line-height:1.1}
.hero-copy{position:absolute;top:170px;width:100%;text-align:center;color:#fff}
.hero-copy h1{font-size:40px;font-weight:700;letter-spacing:2px}
.hero-copy p{margin-top:18px;font-size:18px;line-height:1.7}

.sidebar{position:absolute;left:68px;top:780px;width:240px}
.side-nav{list-style:none}
.side-nav li{display:flex;align-items:center;gap:12px;height:50px;font-size:17px;font-weight:500;border-bottom:1px dotted var(--rule)}
.side-nav .dot{width:34px;height:34px;border-radius:50%;background:var(--teal);flex:none;display:flex;align-items:center;justify-content:center}
.promo{display:flex;align-items:center;justify-content:center;background:linear-gradient(90deg,var(--navy),var(--navy-light));color:#fff;font-weight:700}
.side-promo{margin-top:18px;height:62px;font-size:16px}
.sponsor{margin-top:40px;text-align:center;font-size:12px;color:var(--muted)}
.ad-box{margin:8px auto 0;width:200px;height:240px;border:1px solid var(--rule);background:#fff;text-align:center;padding-top:54px;font-size:15px;color:var(--muted);line-height:1.8}
.ad-box .ad-head{font-size:22px;color:#555}
.ad-box .ad-head strong{font-weight:700}

.main{position:absolute;left:432px;top:780px;width:700px;display:flex;flex-direction:column}
.card{width:700px;background:var(--card);box-shadow:0 1px 4px rgba(0,0,0,.12);padding:36px 40px 40px}
.card + .card{margin-top:30px}
.card h2{font-size:28px;font-weight:700;line-height:1.3;border-left:6px solid var(--accent);margin-left:-40px;padding:0 0 14px 34px;border-bottom:1px solid var(--rule)}
.card p{margin-top:20px;font-size:15px;line-height:1.9;color:var(--muted)}
.card p b{color:var(--ink)}
.card-intro{min-height:250px}
.card-kinds{min-height:610px}
.card-apply{min-height:300px;margin-top:50px !important}
.card-repay{min-height:360px}

.kinds{display:flex;justify-content:space-between;margin-top:36px}
.kind{width:186px;height:186px;border-radius:50%;background:var(--leaf);border:4px solid var(--leaf-line);display:flex;flex-direction:column;align-items:center;justify-content:center}
.kind strong{font-size:34px;font-weight:700;color:var(--leaf-ink);line-height:1.2}
.kind span{font-size:16px;color:var(--leaf-ink);margin-top:4px}

.main-promo{margin-top:24px;width:700px;height:80px;font-size:22px}

.bottom-ad{position:absolute;left:0;top:2640px;width:1200px;text-align:center}
.bottom-ad .sponsor{margin:0}
.ad-strip{margin:8px auto 0;width:700px;height:56px;background:#fff;border:1px solid var(--rule);display:flex;align-items:center;justify-content:space-between;padding:0 16px;font-size:15px;color:var(--muted)}
.ad-strip .btn{background:var(--cta);color:#fff;padding:6px 14px;font-size:14px}

.footer{position:absolute;left:0;top:2780px;width:1200px;height:280px;background:var(--teal);color:#fff}
.footer-cols{display:flex;gap:60px;padding:30px 68px 0}
.footer-cols ul{list-style:none;font-size:13px;line-height:1.9}
.footer-cols li:first-child{font-weight:700}
.copyright{position:absolute;bottom:0;width:100%;height:44px;background:var(--teal-dark);font-size:12px;text-align:center;line-height:44px}
</style>
</head>
<body>

<header class="hero" role="img" aria-label="青空の下で学生たちが跳び上がる写真">
  <div class="brand">
    <div class="brand-mark"></div>
    <div>
      <div class="brand-tag">奨学金制度がよくわかるサイト</div>
      <div class="brand-name">奨学金ガイド</div>
    </div>
  </div>
  <div class="hero-copy">
    <h1>奨学金を知って、上手に活用！</h1>
    <p>「学費が高いから」と進学を諦める前に、<br>自分に合う奨学金制度を見つけてみましょう。</p>
  </div>
</header>

<aside class="sidebar">
  <ul class="side-nav">
    <li><span class="dot"><svg width="16" height="16"><text x="8" y="13" font-size="14" fill="#fff" text-anchor="middle">?</text></svg></span>奨学金とは？</li>
    <li><span class="dot"><svg width="16" height="16"><rect x="2" y="3" width="12" height="10" fill="none" stroke="#fff" stroke-width="2"/></svg></span>奨学金の種類</li>
    <li><span class="dot"><svg width="16" height="16"><circle cx="8" cy="8" r="6" fill="none" stroke="#fff" stroke-width="2"/></svg></span>奨学金の借り方</li>
    <li><span class="dot"><svg width="16" height="16"><path d="M3 8h10M9 4l4 4-4 4" fill="none" stroke="#fff" stroke-width="2"/></svg></span>奨学金の返済方法</li>
    <li><span class="dot"><svg width="16" height="16"><text x="8" y="13" font-size="13" fill="#fff" text-anchor="middle">Q</text></svg></span>よくある質問</li>
  </ul>
  <div class="promo side-promo">新聞奨学金 資料請求</div>
  <div class="sponsor">スポンサーリンク</div>
  <div class="ad-box"><div class="ad-head"><strong>Adplace</strong> に</div>広告を掲載<br>今なら500円で<br>1000円分の広告を</div>
</aside>

<main class="main">
  <section class="card card-intro">
    <h2>奨学金制度のしくみ</h2>
    <p>奨学金制度は、国や地方自治体、民間団体のほか、学校単位でも独自の奨学金制度を設けています。各奨学金の申し込み基準や審査をクリアすれば、誰でも「進学に必要な金銭的サポート」が受けられる仕組みです。</p>
    <p>このように、学生の能力に合わせた奨学金制度、交通災害遺児のための奨学金、海外留学のための奨学金制度もあります。</p>
  </section>

  <section class="card card-kinds">
    <h2>給付方法は二種類</h2>
    <p>奨学金制度は、大きく分けて二つに分類できます。</p>
    <p>一つ目は、<b>貸与（たいよ）</b>と呼ばれる給付の方法で、名前の通り「学費を借りる」奨学金制度です。二つ目は、<b>給付（きゅうふ）</b>と呼ばれる方法で、返済の必要がない奨学金制度です。</p>
    <p>「貸与型」奨学金制度にも、返し方が利息付きのもの（有利子）と、利息の付かない（無利子）ものの二種類があります。</p>
    <div class="kinds">
      <div class="kind"><strong>稼ぐ</strong><span>「奨学金」</span></div>
      <div class="kind"><strong>借りる</strong><span>「奨学金」</span></div>
      <div class="kind"><strong>もらう</strong><span>「奨学金」</span></div>
    </div>
  </section>

  <div class="promo main-promo">新聞奨学金 資料請求</div>

  <section class="card card-apply">
    <h2>奨学金を受けるには？</h2>
    <p>まずは、自分の目的に合う<b>貸与制度（奨学金）</b>を見つけましょう。各奨学金の<b>「募集要項」</b>を確認し、必要書類を準備して所定の期日までに申し込みを行ってください。</p>
    <p>奨学金の審査に通ると、必要な学費のサポート（貸与もしくは給付）が受けられます。</p>
  </section>

  <section class="card card-repay">
    <h2>奨学金返済の仕方</h2>
    <p>奨学金の返済は、学校の卒業後に返済する制度と、学業と両立して働きながら返済できる制度があります。また、給付（きゅうふ）型の奨学金であれば、返済する義務はありません。</p>
  </section>
</main>

<div class="bottom-ad">
  <div class="sponsor">スポンサーリンク</div>
  <div class="ad-strip"><span>ビジネスに独自ドメインの Mailhub を Adplace Works で</span><span class="btn">無料試用を開始</span></div>
</div>

<footer class="footer">
  <div class="footer-cols">
    <ul><li>奨学金とは</li><li>稼ぐ「奨学金」</li><li>借りる「奨学金」</li><li>もらう「奨学金」</li></ul>
    <ul><li>奨学金の種類</li><li>奨学金の申込方法</li><li>貸与型の制度</li><li>給付型の制度</li><li>新聞奨学金について</li><li>学校独自の制度</li></ul>
    <ul><li>奨学金の返済方法</li><li>返済期間について</li><li>返済が困難な場合</li><li>繰上返済について</li><li>返済猶予の手続き</li><li>減額返還について</li></ul>
    <ul><li>よくある質問</li><li>このサイトについて</li><li>お問い合わせ</li><li>サイトマップ</li></ul>
  </div>
  <div class="copyright">Copyright (C) 奨学金ガイド編集委員会 All Rights Reserved.</div>
</footer>

</body>
</html>
```